Commercial photographer, UAV drone photography & 360 walk-through visuals

I need a business card design that is minimalist but yet pretentiously creative. My target market are architects, designers, advertising agents and marketing managers. It is important to stress that though I am asking for a minimalist design it needs to have creative impact.

Target Market(s)

Architects, interiors designers, web-designers, artists

Contact Information for Business Card

Include my name, mobile [cell] number, email, web page and the company logo. Do not to include a postal address.

Colors

Designer to choose colors to be used in the design.

Requirements
Must have
• The following information is to be included:
• Milo Fenwick
• Photographer
• m: 07812 593174
• e: milo@mfimagery.co.uk
• w: mfimagery.co.uk

```html
<!DOCTYPE html>
<html lang="en">
<head>
<meta charset="utf-8">
<title>MF Imagery – Business Card</title>
<link href="https://fonts.googleapis.com/css2?family=Lato:wght@400;700&display=swap" rel="stylesheet">
<style>
  :root {
    --backdrop: #8a8a8a;
    --card-dark: #3a3a3c;
    --card-light: #ffffff;
    --ink: #1c1c1c;
    --ink-soft: #3a3a3a;
    --paper-text: #f4f4f4;
  }
  * { margin: 0; padding: 0; box-sizing: border-box; }
  html, body { width: 1200px; height: 1200px; overflow: hidden; }
  body {
    background: var(--backdrop);
    font-family: "Lato", sans-serif;
    position: relative;
  }
  .card {
    position: absolute;
    left: 180px;
    width: 840px;
    height: 480px;
    box-shadow: 0 12px 30px rgba(0,0,0,0.35);
  }
  .card--front { top: 70px; background: var(--card-dark); }
  .card--back { top: 650px; background: var(--card-light); }

  .brand {
    display: flex;
    align-items: center;
    gap: 16px;
    letter-spacing: 0.14em;
    text-transform: uppercase;
    font-weight: 400;
    white-space: nowrap;
  }
  .brand__dot {
    border-radius: 50%;
    flex: none;
  }
  .card--front .brand {
    position: absolute;
    left: 50%;
    top: 50%;
    transform: translate(-50%, -50%);
    color: var(--paper-text);
    font-size: 54px;
  }
  .card--front .brand__dot { width: 22px; height: 22px; background: var(--paper-text); }

  .frame {
    position: absolute;
    inset: 28px;
    border: 3px solid var(--ink);
  }
  .card--back .brand {
    position: absolute;
    left: 120px;
    top: 80px;
    color: var(--ink);
    font-size: 46px;
  }
  .card--back .brand__dot { width: 18px; height: 18px; background: var(--ink); }

  .details {
    position: absolute;
    left: 120px;
    top: 230px;
    display: flex;
    align-items: stretch;
    gap: 26px;
    color: var(--ink);
  }
  .person { text-align: right; padding-top: 44px; white-space: nowrap; }
  .person__name { font-size: 30px; letter-spacing: 0.05em; text-transform: uppercase; }
  .person__role { font-size: 19px; color: var(--ink-soft); margin-top: 2px; }
  .details__rule { width: 1.5px; background: var(--ink); }
  .contact { list-style: none; font-size: 21px; line-height: 34px; white-space: nowrap; }
  .contact li { display: flex; align-items: center; gap: 12px; }
  .contact svg { width: 20px; height: 20px; fill: var(--ink); flex: none; }
</style>
</head>
<body>
  <section class="card card--front" aria-label="Card front">
    <div class="brand"><span class="brand__dot"></span><span>MF Imagery</span></div>
  </section>

  <section class="card card--back" aria-label="Card back">
    <div class="frame"></div>
    <div class="brand"><span class="brand__dot"></span><span>MF Imagery</span></div>
    <div class="details">
      <div class="person">
        <p class="person__name">Milo Fenwick</p>
        <p class="person__role">Photographer</p>
      </div>
      <div class="details__rule"></div>
      <ul class="contact">
        <li>
          <svg viewBox="0 0 24 24" aria-hidden="true"><path d="M6.6 10.8a15.1 15.1 0 0 0 6.6 6.6l2.2-2.2a1 1 0 0 1 1-.25 11.4 11.4 0 0 0 3.6.57 1 1 0 0 1 1 1V20a1 1 0 0 1-1 1A17 17 0 0 1 3 4a1 1 0 0 1 1-1h3.5a1 1 0 0 1 1 1c0 1.25.2 2.450.57 3.570a1 1 0 0 1-.25 1z"/></svg>
          <span>07812 593174</span>
        </li>
        <li>
          <svg viewBox="0 0 24 24" aria-hidden="true"><path d="M12 2a10 10 0 1 0 5 18.7l-1-1.7A8 8 0 1 1 20 12v1.2a1.8 1.8 0 0 1-3.6 0V7.5h-2v.9A5 5 0 1 0 15 15.6a3.8 3.8 0 0 0 7-2.4V12A10 10 0 0 0 12 2zm0 13a3 3 0 1 1 0-6 3 3 0 0 1 0 6z"/></svg>
          <span>milo@mfimagery.co.uk</span>
        </li>
        <li>
          <svg viewBox="0 0 24 24" aria-hidden="true"><path d="M12 2a10 10 0 1 0 0 20 10 10 0 0 0 0-20zm6.9 6h-3a15.7 15.7 0 0 0-1.3-3.9A8 8 0 0 1 18.9 8zM12 4c.8 1.2 1.5 2.5 1.9 4h-3.8c.4-1.5 1.1-2.8 1.9-4zM4.3 14a8 8 0 0 1 0-4h3.4a16 16 0 0 0 0 4zm.8 2h3a15.7 15.7 0 0 0 1.3 3.9A8 8 0 0 1 5.1 16zm3-8h-3a8 8 0 0 1 4.3-3.9A15.7 15.7 0 0 0 8.1 8zM12 20c-.8-1.2-1.5-2.5-1.9-4h3.8c-.4 1.5-1.1 2.8-1.9 4zm2.3-6H9.7a14.5 14.5 0 0 1 0-4h4.6a14.5 14.5 0 0 1 0 4zm.3 5.9a15.7 15.7 0 0 0 1.3-3.9h3a8 8 0 0 1-4.3 3.9zm1.7-5.9a16 16 0 0 0 0-4h3.4a8 8 0 0 1 0 4z"/></svg>
          <span>mfimagery.co.uk</span>
        </li>
      </ul>
    </div>
  </section>
</body>
</html>
```